New Business Card Design Project

We require a business card design for Zelvaquin, a newly established Indian company.
Our focus is on the development, manufacturing, and export of a diverse array of pharmaceutical products on a global scale. The card should convey a professional appearance, as our primary markets are in Africa, China, and Southeast Asian nations.
We envision a two-sided business card, with the reverse side dedicated to a logo set against a solid color or an elegantly designed pattern. The corners should be rounded. We would appreciate seeing both horizontal and vertical design options. We trust the designer to utilize their expertise in creating this design.

The content for the business card is included in the attached Word file.

Target Market(s)

Our primary markets are in Africa, China, and Southeast Asian, Latin America, Maldives, Sri Lanka

Industry/Entity Type

Pharmaceutical Manufacturing and Export

Contact Information for Business Card

Colors

Designer to choose colors to be used in the design.

Requirements
Must have
• The reverse side of the business card features solely the logo along with the tagline, "Remedies of Life."
Should not have
• The logo should not exceed two instances, encompassing both the front and back sides of the card.

```html
<!DOCTYPE html>
<html lang="en">
<head>
<meta charset="utf-8">
<title>Zelvaquin Business Card</title>
<link rel="stylesheet" href="https://fonts.googleapis.com/css2?family=Montserrat:wght@700&family=Open+Sans:wght@700&family=Arimo:wght@400&display=swap">
<style>
  :root {
    --brand-blue: #2aa8e0;
    --brand-red: #f0604a;
    --paper: #ffffff;
    --ink-gray: #5a5a5a;
    --rule-gray: #6e6e6e;
    --backdrop: #e9ebee;
  }
  * { margin: 0; padding: 0; box-sizing: border-box; }
  html, body { width: 1200px; height: 900px; overflow: hidden; background: var(--backdrop); }
  .stage {
    width: 1200px; height: 900px;
    display: flex; flex-direction: column; align-items: center; justify-content: center; gap: 40px;
  }
  .card {
    position: relative; width: 700px; height: 400px; border-radius: 22px; overflow: hidden;
    box-shadow: 0 8px 24px rgba(0,0,0,0.12);
  }
  .card--back {
    background: var(--brand-blue);
    display: flex; flex-direction: column; align-items: center; justify-content: center; gap: 14px;
  }
  .back-wordmark {
    font-family: "Montserrat", sans-serif; font-weight: 700; font-size: 78px; line-height: 1;
    color: var(--paper); letter-spacing: 1px;
  }
  .back-tagline {
    font-family: "Arimo", sans-serif; font-size: 22px; color: var(--paper); letter-spacing: 3px;
  }
  .card--front { background: var(--paper); }
  .front-wordmark {
    position: absolute; left: 40px; top: 150px;
    font-family: "Montserrat", sans-serif; font-weight: 700; font-size: 52px; color: var(--brand-blue);
  }
  .divider { position: absolute; left: 340px; top: 120px; width: 2px; height: 150px; background: var(--rule-gray); }
  .contact { position: absolute; left: 370px; top: 122px; }
  .person-name { font-family: "Open Sans", sans-serif; font-weight: 700; font-size: 28px; color: var(--brand-blue); line-height: 1.1; }
  .person-role { font-family: "Arimo", sans-serif; font-size: 19px; color: var(--ink-gray); margin-bottom: 20px; }
  .contact-line {
    display: flex; align-items: center; gap: 10px;
    font-family: "Arimo", sans-serif; font-size: 20px; color: var(--ink-gray); line-height: 30px;
  }
  .contact-line svg { width: 18px; height: 18px; flex: none; }
  .accent { color: var(--brand-blue); }
  .address-band {
    position: absolute; left: 0; top: 300px; width: 530px; height: 42px; background: var(--brand-blue);
    font-family: "Arimo", sans-serif; font-size: 21px; color: var(--paper);
    display: flex; align-items: center; justify-content: flex-end; padding-right: 24px;
  }
  .band-end { position: absolute; left: 538px; top: 300px; width: 162px; height: 42px; background: var(--brand-red); }
</style>
</head>
<body>
<main class="stage">
  <section class="card card--back" aria-label="Card back">
    <span class="back-wordmark">Zelvaquin</span>
    <span class="back-tagline">Remedies of Life</span>
  </section>

  <section class="card card--front" aria-label="Card front">
    <span class="front-wordmark">Zelvaquin</span>
    <div class="divider"></div>
    <div class="contact">
      <p class="person-name">Rohan K. Desai</p>
      <p class="person-role">CEO</p>
      <p class="contact-line">
        <svg viewBox="0 0 24 24" fill="none" stroke="#2aa8e0" stroke-width="2"><path d="M5 3h4l2 5-2.5 1.5a11 11 0 0 0 6 6L16 13l5 2v4a2 2 0 0 1-2 2A16 16 0 0 1 3 5a2 2 0 0 1 2-2z"/></svg>
        +919876543210
      </p>
      <p class="contact-line">
        <svg viewBox="0 0 24 24" fill="none" stroke="#2aa8e0" stroke-width="2"><rect x="2" y="5" width="20" height="14" rx="2"/><path d="M2 6l10 7 10-7"/></svg>
        rdesai@zelvaquin.com
      </p>
      <p class="contact-line">
        <svg viewBox="0 0 24 24" fill="none" stroke="#2aa8e0" stroke-width="2"><circle cx="12" cy="12" r="10"/><path d="M2 12h20M12 2a15 15 0 0 1 0 20M12 2a15 15 0 0 0 0 20"/></svg>
        <span>www.<span class="accent">zelvaquin</span>.com</span>
      </p>
    </div>
    <div class="address-band">12, Lotus Park, Nagpur, 440010, India</div>
    <div class="band-end"></div>
  </section>
</main>
</body>
</html>
```